3 banner themes for healthy foods supplements

Who you are
You are a top professional designer. You eat, sleep and breathe banners. You have them for breakfast, lunch and dinner. You have created so many high quality banners that you stopped counting.
Who we are
We are selling premium nutritional supplements.

Deliverables
We need to design 3 different banner themes, each in the following formats:
- Vertical rectangle: 240 x 400
- Mobile leaderboard: 320 x 50
- Banner: 468 x 60
- Leaderboard: 728 x 90
- Square: 250 x 250
- Small square: 200 x 200
- Large rectangle: 336 x 280
- Inline rectangle: 300 x 250
- Skyscraper: 120 x 600
- Wide skyscraper: 160 x 600
- Half-page: 300 x 600
- Large leaderboard: 970x90
- Large mobile banner: 320 x 100
- Billboard: 970 x 250
- Portrait: 300 x 1050

To give us a taste of your design skills, we invite you to submit one format (300 x 250) of each of the 3 different banner themes described below before we finally give you the green light and award you. Once awarded you should deliver all 3 themes with all above mentioned banner formats.

The final deliverable shall be editable .psd files.

Our products
The products we are advertising are organic, raw, vegan, premium nutritional supplements, such as algae powder, wheat grass powder and goji berries. The products stand to support a healthy life style. Please have a look at our shop. It is in German, but you get the gist. http://www.merolina.-shop.example

The design
We would describe the style of the banners as follows:
- Premium
- Joyful
- White background
- Minimalistic

Each banner theme shall advertise the following messages about the products:
- Product name (chlorella algae powder , wheatgrass powder, goji berries)
- healthy
- 100 % vegan, raw and organic
- 100% natural
- premium product

Each of the above attributes can be represented with labels of different colours, similar to the attached sample files. We like the colour combination of the labels on this banner a lot.
All 3 themes shall contain our logo which you find attached to this job description. The logo shall be visible, but not too prominent.

The only difference between the 3 different themes shall be the product photo and the product name. All other elements on the banner shall be the same.

Theme A
This theme advertises algae powder, such as chlorella algae. The product photo is attached and should of course appear prominently on the banner.

Theme B
This theme advertises wheat grass powder. The product photo is attached and should of course appear prominently on the banner.

Theme C
This theme advertises goji berries. The product photo is attached and should of course appear prominently on the banner.

Target Market(s)

Health conscious people.

Industry/Entity Type

It Professional

Font styles to use
Sans Serif

Colors
00a990
a54499
f37122
fbed22
0692cd
9bcb3b
ffc214

Requirements
Must have
• - product image as per in the attachment
• - logo
• - bright, clear, joyful colors
Should not have
• - heavy dark colors
• - frame

```html
<!DOCTYPE html>
<html lang="en">
<head>
<meta charset="utf-8">
<title>Solvia – Supplement Banner Themes</title>
<link rel="stylesheet" href="https://fonts.googleapis.com/css2?family=Bebas+Neue&display=swap">
<style>
  :root {
    --page: #ffffff;
    --panel: #e1e1e1;
    --header: #ffffff;
    --title: #0d4a34;
    --purple: #a54499;
    --teal: #00a990;
    --green: #9bcb3b;
    --blue: #0692cd;
    --orange: #f37122;
    --label-light: #ffffff;
    --label-dark: #16432a;
  }
  * { margin: 0; padding: 0; box-sizing: border-box; }
  html, body {
    width: 1200px;
    height: 401px;
    overflow: hidden;
    background: var(--page);
    font-family: "Bebas Neue", "Arial Narrow", sans-serif;
  }
  .showcase {
    position: absolute;
    left: 90px;
    top: 50px;
    width: 1020px;
    height: 300px;
    background: var(--panel);
  }
  .banner {
    position: absolute;
    top: 26px;
    width: 300px;
    height: 250px;
    overflow: hidden;
    background: var(--header);
  }
  .banner--wheatgrass { left: 30px; }
  .banner--goji { left: 360px; }
  .banner--chlorella { left: 690px; }

  .banner__header {
    position: relative;
    height: 56px;
    background: var(--header);
  }
  .brand {
    position: absolute;
    left: 10px;
    top: 21px;
    display: flex;
    align-items: center;
    gap: 4px;
    color: var(--title);
    font-size: 14px;
    line-height: 1;
    letter-spacing: 0.5px;
  }
  .brand__dot {
    width: 12px;
    height: 12px;
    border-radius: 50%;
    background: var(--orange);
  }
  .banner__title {
    position: absolute;
    right: 17px;
    top: 0;
    height: 56px;
    display: flex;
    align-items: center;
    color: var(--title);
    font-weight: 400;
    letter-spacing: 1.4px;
    line-height: 1;
    white-space: nowrap;
  }
  .banner--wheatgrass .banner__title { font-size: 25px; letter-spacing: 1.6px; }
  .banner--goji .banner__title { font-size: 38px; right: 15px; letter-spacing: 1.6px; }
  .banner--chlorella .banner__title { font-size: 21.5px; letter-spacing: 1px; }

  .banner__photo {
    position: absolute;
    left: 0;
    top: 56px;
    width: 300px;
    height: 194px;
  }
  .photo--wheatgrass {
    background: radial-gradient(ellipse at 40% 30%, #c3cf8e 0%, #a8b86c 50%, #8f9f56 100%);
  }
  .photo--goji {
    background: radial-gradient(ellipse at 50% 35%, #f0512e 0%, #d9341d 55%, #a3200f 100%);
  }
  .photo--chlorella {
    background: radial-gradient(ellipse at 45% 30%, #3f6a52 0%, #2c5040 55%, #1e3a2c 100%);
  }

  .labels {
    position: absolute;
    left: 0;
    top: 0;
    width: 300px;
    height: 250px;
  }
  .label--purple { fill: var(--purple); }
  .label--teal { fill: var(--teal); }
  .label--green { fill: var(--green); }
  .label--blue { fill: var(--blue); }
  .label-text {
    font-family: "Bebas Neue", "Arial Narrow", sans-serif;
    font-size: 17.5px;
    letter-spacing: 0.5px;
    fill: var(--label-light);
  }
  .label-text--dark { fill: var(--label-dark); }
</style>
</head>
<body>
  <main class="showcase">

    <article class="banner banner--wheatgrass">
      <header class="banner__header">
        <div class="brand"><span class="brand__dot"></span>Solvia</div>
        <h2 class="banner__title">Wheat Grass Powder</h2>
      </header>
      <div class="banner__photo photo--wheatgrass" role="img" aria-label="Close-up photo of pale green wheat grass powder"></div>
      <svg class="labels" viewBox="0 0 300 250">
        <polygon class="label--purple" points="0,157 90,157 80,190 0,190"/>
        <polygon class="label--teal" points="86,157 300,157 300,190 76,190"/>
        <polygon class="label--green" points="0,197 132,197 122,230 0,230"/>
        <polygon class="label--blue" points="129,197 300,197 300,230 119,230"/>
        <text class="label-text" x="12" y="180">Healthy</text>
        <text class="label-text" x="195" y="180" text-anchor="middle">100% Vegan, Raw and Organic</text>
        <text class="label-text label-text--dark" x="18" y="220">100% Natural</text>
        <text class="label-text" x="219" y="220" text-anchor="middle">Premium Product</text>
      </svg>
    </article>

    <article class="banner banner--goji">
      <header class="banner__header">
        <div class="brand"><span class="brand__dot"></span>Solvia</div>
        <h2 class="banner__title">Goji Berries</h2>
      </header>
      <div class="banner__photo photo--goji" role="img" aria-label="Close-up photo of dried red goji berries"></div>
      <svg class="labels" viewBox="0 0 300 250">
        <polygon class="label--purple" points="0,157 90,157 80,190 0,190"/>
        <polygon class="label--teal" points="86,157 300,157 300,190 76,190"/>
        <polygon class="label--green" points="0,197 132,197 122,230 0,230"/>
        <polygon class="label--blue" points="129,197 300,197 300,230 119,230"/>
        <text class="label-text" x="12" y="180">Healthy</text>
        <text class="label-text" x="195" y="180" text-anchor="middle">100% Vegan, Raw and Organic</text>
        <text class="label-text label-text--dark" x="18" y="220">100% Natural</text>
        <text class="label-text" x="219" y="220" text-anchor="middle">Premium Product</text>
      </svg>
    </article>

    <article class="banner banner--chlorella">
      <header class="banner__header">
        <div class="brand"><span class="brand__dot"></span>Solvia</div>
        <h2 class="banner__title">Chlorella Algae Powder</h2>
      </header>
      <div class="banner__photo photo--chlorella" role="img" aria-label="Close-up photo of dark green chlorella algae powder"></div>
      <svg class="labels" viewBox="0 0 300 250">
        <polygon class="label--purple" points="0,157 90,157 80,190 0,190"/>
        <polygon class="label--teal" points="86,157 300,157 300,190 76,190"/>
        <polygon class="label--green" points="0,197 132,197 122,230 0,230"/>
        <polygon class="label--blue" points="129,197 300,197 300,230 119,230"/>
        <text class="label-text" x="12" y="180">Healthy</text>
        <text class="label-text" x="195" y="180" text-anchor="middle">100% Vegan, Raw and Organic</text>
        <text class="label-text label-text--dark" x="18" y="220">100% Natural</text>
        <text class="label-text" x="219" y="220" text-anchor="middle">Premium Product</text>
      </svg>
    </article>

  </main>
</body>
</html>
```